Label for Refill packaging eco-conscious beauty brand

We need a label for our refill pouch. Velvet Harbor is an unscented conditioner formulated using the finest healthy & pure ingredients, free of chemicals and harmful toxins. As a minimalist beauty brand we are proud to be certified with TQB, Norvamark and Silver Kestrel.

We already have the pouches and an exciting label for our regular bottles.
We choose a kraft brown packing for the refill pouch and would like something minimalist but elegant for the label.

```html
<!DOCTYPE html>
<html lang="en">
<head>
<meta charset="utf-8">
<title>Velvet Harbor – refill label</title>
<link rel="stylesheet" href="https://fonts.googleapis.com/css2?family=Montserrat:wght@300;400&display=swap">
<style>
  :root {
    --backdrop: #ecebe8;
    --sage-top: #5c6661;
    --sage-bottom: #6d736e;
    --umber-top: #55503f;
    --umber-bottom: #6f675a;
    --gold-light: #e0bd4e;
    --gold-dark: #b58a1f;
    --ink-light: #f4f2ee;
    --leaf-tone: rgba(40, 40, 36, 0.22);
  }
  * { margin: 0; padding: 0; box-sizing: border-box; }
  html, body {
    width: 1200px; height: 800px; overflow: hidden;
    background: var(--backdrop);
    font-family: "Montserrat", Arial, sans-serif;
  }
  .label-sheet {
    width: 1200px; height: 800px;
    display: flex; justify-content: center; align-items: center; gap: 80px;
  }
  .refill-label {
    position: relative;
    width: 360px; height: 660px;
    color: var(--ink-light);
    text-align: center;
    overflow: hidden;
  }
  .refill-label--sage { background: linear-gradient(160deg, var(--sage-top), var(--sage-bottom)); }
  .refill-label--umber { background: linear-gradient(160deg, var(--umber-top), var(--umber-bottom)); }
  .leaf-art {
    position: absolute; left: 20px; top: 100px;
    width: 320px; height: 520px;
  }
  .brand-mark {
    position: absolute; left: 50%; transform: translateX(-50%);
    top: 48px;
    display: flex; flex-direction: column; align-items: center; gap: 14px;
  }
  .refill-label--umber .brand-mark {
    top: 36px;
    width: 88px; padding: 16px 0 14px;
    background: linear-gradient(135deg, var(--gold-light), var(--gold-dark));
  }
  .brand-mark__square {
    width: 46px; height: 46px;
    border: 1.5px solid var(--ink-light);
  }
  .brand-mark__name {
    font-weight: 300; font-size: 21px; line-height: 1.2; letter-spacing: 0.5px;
  }
  .product-name {
    position: absolute; left: 0; right: 0; top: 262px;
    font-weight: 300; font-size: 60px; line-height: 1.08; letter-spacing: 0.5px;
  }
  .product-desc {
    position: absolute; left: 0; right: 0; top: 440px;
    font-weight: 300; font-size: 13px; line-height: 1.1;
  }
  .refill-tag {
    position: absolute; left: 0; right: 0; top: 580px;
    font-weight: 300; font-size: 13px;
  }
  .net-volume {
    position: absolute; left: 0; right: 0; top: 608px;
    font-weight: 300; font-size: 13px;
  }
</style>
</head>
<body>
<main class="label-sheet">
  <article class="refill-label refill-label--sage">
    <svg class="leaf-art" viewBox="0 0 320 520" role="img" aria-label="Fine line skeleton leaf illustration">
      <defs>
        <linearGradient id="leafSage" x1="0" y1="0" x2="1" y2="1">
          <stop offset="0" stop-color="#2e3430" stop-opacity="0.18"/>
          <stop offset="1" stop-color="#2e3430" stop-opacity="0.28"/>
        </linearGradient>
      </defs>
      <ellipse cx="160" cy="275" rx="125" ry="250" transform="rotate(-24 160 275)" fill="url(#leafSage)"/>
    </svg>
    <div class="brand-mark">
      <span class="brand-mark__square"></span>
      <span class="brand-mark__name">KELDA<br>Moss</span>
    </div>
    <h1 class="product-name">Velvet<br>Harbor</h1>
    <p class="product-desc">unscented hair conditioner<br>après-shampoing non parfumé</p>
    <p class="refill-tag">refill</p>
    <p class="net-volume">238ml ℮ / 8fl.oz</p>
  </article>

  <article class="refill-label refill-label--umber">
    <svg class="leaf-art" viewBox="0 0 320 520" role="img" aria-label="Fine line skeleton leaf illustration">
      <defs>
        <linearGradient id="leafUmber" x1="0" y1="0" x2="1" y2="1">
          <stop offset="0" stop-color="#2a261f" stop-opacity="0.2"/>
          <stop offset="1" stop-color="#2a261f" stop-opacity="0.3"/>
        </linearGradient>
      </defs>
      <ellipse cx="160" cy="275" rx="125" ry="250" transform="rotate(-24 160 275)" fill="url(#leafUmber)"/>
    </svg>
    <div class="brand-mark">
      <span class="brand-mark__square"></span>
      <span class="brand-mark__name">KELDA<br>Moss</span>
    </div>
    <h1 class="product-name">Velvet<br>Harbor</h1>
    <p class="product-desc">unscented hair conditioner<br>après-shampoing non parfumé</p>
    <p class="refill-tag">refill</p>
    <p class="net-volume">238ml ℮ / 8fl.oz</p>
  </article>
</main>
</body>
</html>
```